Veltoran cost over-runs infographic

I need an infographic about the potential 2026 Calgary Veltoran winter games bid. I'd like to use some stylized cartoon-ish graphics of Calgary, Canada landmarks in the background and/or veltoran sport cartoon-ish graphics and then show the cost overruns from the last 10 winter veltorans as detailed on table 3 in this report: http://archive.brennick-study.example/4821/1/2016-20.pdf

Maybe a bar chart or some other visualization of the cost overruns.

And maybe stick Calgary in there with a question mark next to it.

Size of the graphic should be 5" x 6.7" and high dpi suitable for print.

```html
<!DOCTYPE html>
<html lang="en">
<head>
<meta charset="utf-8">
<title>Cost Overruns of the 1980-2014 Winter Veltorans</title>
<link rel="stylesheet" href="https://fonts.googleapis.com/css2?family=Montserrat:wght@500;600;700;800&display=swap">
<style>
  :root {
    --header-blue: #1a8ad4;
    --header-deep: #0f6fb3;
    --sky-top: #d6effb;
    --sky-bottom: #a9dcf4;
    --avg-band: #a8d8f4;
    --median-band: #f9d2a5;
    --median-brown: #a66a3a;
    --bar-red: #e0242b;
    --city-blue: #1f93da;
    --city-border: #1b4f7a;
    --country-yellow: #fbee8a;
    --year-purple: #7f6cae;
    --ink-navy: #2f3a8a;
    --ink-dark: #1c2436;
    --white: #ffffff;
  }
  * { margin: 0; padding: 0; box-sizing: border-box; }
  html, body { width: 896px; height: 1200px; overflow: hidden; }
  body { font-family: "Montserrat", Arial, sans-serif; background: var(--sky-top); }
  .canvas {
    position: relative; width: 896px; height: 1200px; overflow: hidden;
    background: linear-gradient(180deg, var(--sky-top) 0%, #cbe9f8 60%, var(--sky-bottom) 100%);
  }
  .header {
    position: absolute; left: 0; top: 0; width: 896px; height: 128px;
    background: linear-gradient(90deg, var(--header-blue), var(--header-deep));
    text-align: center; color: var(--white); z-index: 1;
  }
  .header h1 { font-size: 55px; font-weight: 800; letter-spacing: 1px; line-height: 1; padding-top: 22px; margin-left: -8px; }
  .header p { font-size: 24px; font-weight: 800; letter-spacing: 0.5px; margin-top: 6px; margin-left: -8px; }
  .trend-arrow { position: absolute; left: 0; top: 0; z-index: 2; }

  .avg-band { position: absolute; left: 313px; top: 210px; width: 192px; height: 785px; background: var(--avg-band); }
  .median-band { position: absolute; left: 505px; top: 210px; width: 40px; height: 828px; background: var(--median-band); }
  .art-panel {
    position: absolute; left: 546px; top: 210px; width: 350px; height: 870px;
    border-left: 3px solid var(--header-deep);
    background: linear-gradient(160deg, #ffffff 0%, #e9f4fb 45%, #c9e3f3 100%);
  }
  .art-panel .figure {
    position: absolute; left: 20px; top: 40px; width: 320px; height: 640px;
    background: linear-gradient(200deg, rgba(120,170,230,0.55), rgba(230,120,190,0.45) 45%, rgba(90,200,220,0.35) 80%, rgba(255,255,255,0));
    border-radius: 160px 160px 40px 40px;
  }

  .row { position: absolute; left: 57px; height: 56px; width: 820px; z-index: 3; }
  .place { position: absolute; left: 0; top: 0; width: 183px; }
  .place .city {
    height: 28px; background: var(--city-blue); border: 2px solid var(--city-border); border-bottom: none;
    color: var(--white); font-size: 21px; font-weight: 700; padding-left: 8px; line-height: 25px;
  }
  .place .country {
    height: 27px; background: var(--country-yellow); border: 2px solid var(--city-border);
    color: var(--ink-dark); font-size: 15px; font-weight: 500; padding-left: 8px; line-height: 23px;
  }
  .row.future .city { background: var(--bar-red); }
  .year {
    position: absolute; left: 183px; top: 12px; width: 73px; height: 40px;
    background: var(--year-purple); color: var(--white); font-size: 23px; font-weight: 600;
    line-height: 40px; text-align: center;
  }
  .bar {
    position: absolute; left: 256px; top: 10px; height: 44px; background: var(--bar-red);
    border: 1px solid var(--white);
    display: flex; align-items: center; justify-content: flex-end; padding-right: 8px;
    color: var(--white); font-size: 35px; font-weight: 800;
  }
  .bar .tip { width: 0; height: 0; border-top: 9px solid transparent; border-bottom: 9px solid transparent; border-left: 11px solid var(--white); margin-left: 12px; }
  .value-out { position: absolute; top: 12px; color: var(--ink-navy); font-size: 33px; font-weight: 800; line-height: 40px; }
  .unknown { position: absolute; left: 272px; top: -6px; color: #8b1d24; font-size: 58px; font-weight: 800; letter-spacing: 2px; }

  .stat-label { position: absolute; color: var(--ink-navy); font-size: 29px; font-weight: 800; transform: rotate(90deg); transform-origin: left top; z-index: 3; }
  .stat-average { left: 512px; top: 722px; }
  .stat-median { left: 547px; top: 775px; color: #8b2f2a; }

  .legend { position: absolute; height: 40px; color: var(--white); font-size: 21px; font-weight: 700; display: flex; align-items: center; padding-left: 14px; z-index: 4; }
  .legend .tip { width: 0; height: 0; border-top: 9px solid transparent; border-bottom: 9px solid transparent; border-left: 11px solid var(--ink-dark); }
  .legend-average { left: 313px; top: 996px; width: 192px; background: var(--header-deep); padding-left: 38px; justify-content: space-between; padding-right: 4px; }
  .legend-median { left: 370px; top: 1037px; width: 175px; background: var(--median-brown); padding-left: 36px; justify-content: space-between; padding-right: 4px; }
  .legend-overrun { left: 405px; top: 1077px; width: 300px; background: var(--bar-red); padding-left: 48px; gap: 8px; }
  .legend-overrun .tips { position: absolute; left: 300px; top: 11px; display: flex; gap: 2px; }
  .legend-overrun .tips i { display: block; width: 0; height: 0; border-top: 9px solid transparent; border-bottom: 9px solid transparent; border-left: 11px solid var(--ink-dark); }
  .legend-overrun .tips i:nth-child(2) { border-left-color: #f08a24; }
  .legend-overrun .tips i:nth-child(3) { border-left-color: var(--bar-red); }

  .brand { position: absolute; left: 600px; top: 965px; display: flex; align-items: center; gap: 14px; color: var(--ink-dark); font-size: 38px; font-weight: 700; z-index: 3; }
  .brand .dot { width: 34px; height: 34px; border-radius: 50%; background: var(--city-blue); }

  .sports-scene {
    position: absolute; left: 0; top: 990px; width: 300px; height: 210px; z-index: 1;
    background: radial-gradient(ellipse at 45% 55%, rgba(20,40,70,0.45), rgba(60,140,200,0.25) 55%, rgba(255,255,255,0) 75%);
  }
  .skyline {
    position: absolute; left: 0; top: 1120px; width: 896px; height: 80px; z-index: 1;
    background: linear-gradient(180deg, rgba(90,190,235,0.55), rgba(40,160,225,0.85));
  }
</style>
</head>
<body>
<div class="canvas">
  <header class="header">
    <h1>COST OVERRUNS</h1>
    <p>OF THE 1980-2014 WINTER VELTORANS</p>
  </header>
  <svg class="trend-arrow" width="896" height="170" viewBox="0 0 896 170" aria-hidden="true">
    <polygon points="320,162 320,158 770,128 800,100 788,38 872,36 872,122 846,96 800,148" fill="#e0242b"/>
  </svg>

  <div class="avg-band"></div>
  <div class="median-band"></div>
  <div class="art-panel">
    <div class="figure" role="img" aria-label="Colourful sketch of a ski jumper in flight"></div>
  </div>

  <div class="row" style="top:160px"><div class="place"><div class="city">Lake Placid</div><div class="country">United States</div></div><div class="year">1980</div><div class="bar" style="width:532px">324<span class="tip"></span></div></div>
  <div class="row" style="top:237px"><div class="place"><div class="city">Sarajevo</div><div class="country">Yugoslavia</div></div><div class="year">1984</div><div class="bar" style="width:194px">118<span class="tip"></span></div></div>
  <div class="row" style="top:313px"><div class="place"><div class="city">Calgary</div><div class="country">Canada</div></div><div class="year">1988</div><div class="bar" style="width:107px">65<span class="tip"></span></div></div>
  <div class="row" style="top:390px"><div class="place"><div class="city">Albertville</div><div class="country">France</div></div><div class="year">1992</div><div class="bar" style="width:225px">137<span class="tip"></span></div></div>
  <div class="row" style="top:466px"><div class="place"><div class="city">Lillehammer</div><div class="country">Norway</div></div><div class="year">1994</div><div class="bar" style="width:454px">277<span class="tip"></span></div></div>
  <div class="row" style="top:543px"><div class="place"><div class="city">Nagano</div><div class="country">Japan</div></div><div class="year">1998</div><div class="bar" style="width:92px">56<span class="tip"></span></div></div>
  <div class="row" style="top:620px"><div class="place"><div class="city">Salt Lake City</div><div class="country">United States</div></div><div class="year">2002</div><div class="bar" style="width:40px;padding-right:6px"><span class="tip" style="margin:0"></span></div><div class="value-out" style="left:305px">24</div></div>
  <div class="row" style="top:697px"><div class="place"><div class="city">Torino</div><div class="country">Italy</div></div><div class="year">2006</div><div class="bar" style="width:131px">80<span class="tip"></span></div></div>
  <div class="row" style="top:772px"><div class="place"><div class="city">Vancouver</div><div class="country">Canada</div></div><div class="year">2010</div><div class="bar" style="width:22px;padding-right:3px"><span class="tip" style="margin:0"></span></div><div class="value-out" style="left:284px">13</div></div>
  <div class="row" style="top:849px"><div class="place"><div class="city">Sochi</div><div class="country">Russia</div></div><div class="year">2014</div><div class="bar" style="width:474px">289<span class="tip"></span></div></div>
  <div class="row future" style="top:926px"><div class="place"><div class="city">CALGARY</div><div class="country">Canada</div></div><div class="year">2026</div><div class="unknown">???</div></div>

  <div class="stat-label stat-average">142</div>
  <div class="stat-label stat-median">118</div>

  <div class="skyline" role="img" aria-label="Blue silhouette of the Calgary city skyline"></div>
  <div class="sports-scene" role="img" aria-label="Silhouettes of winter athletes: hockey player, snowboarder, skier, biathlete and skater"></div>

  <div class="legend legend-average"><span>AVERAGE</span><span class="tip"></span></div>
  <div class="legend legend-median"><span>MEDIAN</span><span class="tip"></span></div>
  <div class="legend legend-overrun"><span>COST OVERRUN %</span><span class="tips"><i></i><i></i><i></i></span></div>

  <div class="brand"><span class="dot"></span><span>Veltoran</span></div>
</div>
</body>
</html>
```